Concierge Healthcare Business Card Design and Logo

We need a logo and business card design for a new company called "Sound Keeper". We will provide concierge audiological care, hearing aids, hearing exams, custom hearing protection etc to patients in the comfort of their homes and offices. We would like a sleek and modern design preferably with an Ear related logo.

Target Market(s)

People with hearing loss, Hunters, Musicians
My usual clientele are older individuals so usually 50+ years old

Industry/Entity Type

Health Care

Contact Information for Business Card

Clara Whitfield, AuD
Audiologist
512-418-2967
soundkeeper@mailvista.net
www.soundkeeperclinic.net

Logo Text

Sound Keeper

Number of Pages Required

3 page

```html
<!DOCTYPE html>
<html lang="en">
<head>
<meta charset="utf-8">
<title>Sound Keeper – Business Card</title>
<link rel="stylesheet" href="https://fonts.googleapis.com/css2?family=Jost:wght@300;400&display=swap">
<style>
  :root {
    --page-bg: #f6f6f6;
    --teal: #137f96;
    --teal-mark: #1a8ea6;
    --front-text: #e6eef0;
    --back-paper: #e9e9e9;
    --back-brand: #6a6a6a;
    --back-text: #222222;
    --divider: #b9b9b9;
  }
  html, body {
    margin: 0;
    padding: 0;
    width: 1016px;
    height: 1200px;
    overflow: hidden;
    background: var(--page-bg);
    font-family: "Jost", "Futura", sans-serif;
  }
  .card {
    position: absolute;
    left: 64px;
    width: 888px;
    box-sizing: border-box;
  }
  .card-front {
    top: 46px;
    height: 516px;
    background: var(--teal);
  }
  .card-back {
    top: 600px;
    height: 520px;
    background: var(--back-paper);
  }
  .brand-mark {
    position: absolute;
    border-radius: 50%;
  }
  .card-front .brand-mark {
    left: 384px;
    top: 168px;
    width: 120px;
    height: 120px;
    background: var(--teal-mark);
    box-shadow: inset 0 3px 8px rgba(0,0,0,0.25);
  }
  .brand-name {
    position: absolute;
    margin: 0;
    font-weight: 300;
    text-transform: uppercase;
    white-space: nowrap;
    text-align: center;
  }
  .card-front .brand-name {
    left: 0;
    right: 0;
    top: 372px;
    font-size: 36px;
    letter-spacing: 4px;
    color: var(--front-text);
  }
  .card-back .brand-mark {
    left: 246px;
    top: 166px;
    width: 52px;
    height: 52px;
    background: var(--teal);
  }
  .card-back .brand-name {
    left: 62px;
    width: 420px;
    top: 268px;
    font-size: 34px;
    letter-spacing: 3px;
    color: var(--back-brand);
  }
  .divider {
    position: absolute;
    left: 440px;
    top: 124px;
    width: 1px;
    height: 284px;
    background: var(--divider);
  }
  .contact {
    position: absolute;
    left: 488px;
    top: 144px;
    margin: 0;
    padding: 0;
    list-style: none;
    color: var(--back-text);
    font-size: 23px;
    font-weight: 400;
    letter-spacing: 1.4px;
    line-height: 43px;
  }
</style>
</head>
<body>
  <section class="card card-front">
    <span class="brand-mark" aria-hidden="true"></span>
    <h1 class="brand-name">Sound Keeper</h1>
  </section>

  <section class="card card-back">
    <span class="brand-mark" aria-hidden="true"></span>
    <p class="brand-name">Sound Keeper</p>
    <span class="divider" aria-hidden="true"></span>
    <ul class="contact">
      <li class="contact-name">Clara Whitfield, AuD</li>
      <li class="contact-role">Audiologist</li>
      <li class="contact-phone">512-418-2967</li>
      <li class="contact-email">soundkeeper@mailvista.net</li>
      <li class="contact-web">www.soundkeeperclinic.net</li>
    </ul>
  </section>
</body>
</html>
```